Landing page for buying gold and stamps

Create a landing page for our purchase. We buy postage stamps, franked goods, gold coins, scrap gold, silver money, etc. We don't want to sell anything to people, we just shop. So the visitors should send their old gold, their stamps, etc. by post. We then estimate the value and transfer the money by bank or you can collect it in cash.

The visitor should see what he can sell. If he fills in his contact details, he will receive our purchase form and the mailing label by post so that he can send in his sales goods free of charge. Or he can call us or write an e-mail and come to us directly.

We buy:
When the form is filled out, an email will be sent to our address with the following data:
Surname
First name
Street, Nr.
Post loan number
place
What do you want to sell

In the appendix I have added designs of flyers. You can see what we buy on it. What is missing on the flyer, however, are stamps, franking goods and rarities. In addition, the design should be similar. The logo can also be used.

In addition, the following text should be on the page:
Do you need help selling an inherited collection? Feel free to contact us. We are happy to help. We have been in the stamp and coin trade for nearly 100 years.

I have also attached a picture of the stamp as an attachment. This should also be put on the side with old gold and gold coins.

And here you will find our current purchase pages:
https://www.briefhaus-tanner.ch/ankauf-gold-und-silber
https://www.briefhaus-tanner.ch/ankauf-frankatur

Competitors' pages:
https://www.wertsachenpost.ch/goldankauf/
https://www.praegehof-lindt.ch/ankauf-1/altgold-ankauf1.html

Target Market(s)

Private persons

Font styles to use
Serif
Sans Serif

Requirements
Must have
• It must be clear that anyone who wants to sell their gold, stamps or coins can do so easily from home by post. You no longer have to go to a store.
Steps to Sell:
1. You fill out your contact details
2. We will send you a form and a label for shipping (no postage for you!)
3. You will receive a non-binding purchase offer
4. You will receive the money transferred or you can collect it in cash (or we will send you the valuables you have sent back)

You have no costs! Simply sell your gold or stamps from home.

```html
<!DOCTYPE html>
<html lang="en">
<head>
<meta charset="utf-8">
<title>Briefhaus Tanner – We buy gold, silver and stamps</title>
<link rel="stylesheet" href="https://fonts.googleapis.com/css2?family=Merriweather:wght@700;900&family=Montserrat:wght@400;500&display=swap">
<style>
:root{
  --gold:#f9b806;
  --brown-dark:#3f2e21;
  --brown-hero:#7a5a3e;
  --ink:#1c1c1c;
  --text:#4a4a4a;
  --muted:#7b7b7b;
  --soft-bg:#f4f4f6;
  --white:#ffffff;
  --serif:'Merriweather', Georgia, serif;
  --sans:'Montserrat', Arial, sans-serif;
}
*{box-sizing:border-box;margin:0;padding:0}
html,body{width:1200px;height:2704px;overflow:hidden}
body{position:relative;font-family:var(--sans);color:var(--text);background:var(--white)}
.btn{position:absolute;display:flex;align-items:center;justify-content:center;background:var(--gold);color:var(--white);font-family:var(--serif);font-weight:700;font-size:19px;width:152px;height:48px;text-decoration:none}

/* Hero */
.hero{position:absolute;left:0;top:0;width:1200px;height:631px;
  background:radial-gradient(ellipse at 30% 20%,#8e6a4b 0%,#7a5a3e 45%,#5a3f2a 80%,#3d2a1c 100%);overflow:hidden}
.hero-coin{position:absolute;left:656px;top:133px;width:452px;height:452px;border-radius:50%;
  background:radial-gradient(circle at 40% 38%,#e8bd5a 0%,#c99639 45%,#9b6b23 80%,#6f4a17 100%);
  box-shadow:0 20px 40px rgba(0,0,0,.35)}
.brand{position:absolute;left:91px;top:19px;height:46px;display:flex;align-items:center;gap:10px;
  font-family:var(--serif);font-weight:700;font-size:22px;color:var(--white)}
.brand-mark{width:18px;height:18px;background:var(--gold)}
.hero-title{position:absolute;left:82px;top:172px;width:620px;font-family:var(--serif);font-weight:700;
  font-size:58px;line-height:68px;color:var(--white)}
.hero-text{position:absolute;left:83px;top:335px;width:470px;font-size:15px;line-height:23px;color:var(--white)}
.hero-text a{color:var(--gold);text-decoration:none}
.hero-icon{position:absolute;top:474px;width:24px;height:24px}

/* How we work */
.steps{position:absolute;left:0;top:631px;width:1200px;height:413px;background:var(--soft-bg)}
.section-title{font-family:var(--serif);font-weight:700;font-size:40px;color:var(--ink)}
.steps .section-title{position:absolute;top:50px;width:100%;text-align:center}
.step-line{position:absolute;top:163px;left:250px;width:700px;border-top:2px dotted #d3d3d9}
.step{position:absolute;top:124px;width:250px;text-align:center}
.step-icon{width:84px;height:84px;border-radius:50%;background:var(--white);margin:0 auto;
  box-shadow:0 8px 18px rgba(0,0,0,.12);display:flex;align-items:center;justify-content:center}
.step-name{margin-top:30px;font-family:var(--serif);font-weight:700;font-size:20px;color:var(--ink)}
.step-text{margin-top:14px;font-size:15px;line-height:23px;color:var(--text)}

/* What we buy */
.buy{position:absolute;left:0;top:1044px;width:1200px;height:833px;background:var(--white);overflow:hidden}
.buy .section-title{position:absolute;left:82px;top:68px}
.buy-card{position:absolute;overflow:hidden}
.buy-card span{position:absolute;left:25px;bottom:30px;font-size:32px;font-weight:500;color:var(--white)}
.deco-ring{position:absolute;border-radius:50%;border:36px solid rgba(236,236,240,.7)}

/* CTA band */
.cta{position:absolute;left:0;top:1877px;width:1200px;height:215px;background:var(--brown-dark)}
.cta-title{position:absolute;left:79px;top:82px;font-family:var(--serif);font-weight:700;font-size:42px;color:var(--white)}

/* Testimonials */
.voices{position:absolute;left:0;top:2092px;width:1200px;height:553px;background:var(--soft-bg);overflow:hidden}
.voices .section-title{position:absolute;top:48px;width:100%;text-align:center}
.voices-sub{position:absolute;top:120px;width:100%;text-align:center;font-size:15px;color:var(--text)}
.quote{position:absolute;top:174px;width:292px;height:159px;background:var(--white);text-align:center;padding:40px 26px 0}
.quote::after{content:"";position:absolute;left:50%;bottom:-10px;margin-left:-10px;border:10px solid transparent;border-bottom:0;border-top-color:var(--white)}
.quote h3{font-family:var(--serif);font-weight:700;font-size:20px;color:var(--ink)}
.quote p{margin-top:10px;font-size:11.5px;line-height:17.5px;color:var(--text)}
.person{position:absolute;top:357px;width:292px;text-align:center}
.avatar{width:46px;height:46px;border-radius:50%;margin:0 auto;background:linear-gradient(160deg,#8a6b58,#4a3a33)}
.person b{display:block;margin-top:6px;font-family:var(--serif);font-size:14px;color:var(--ink)}
.person small{display:block;font-size:12px;color:var(--muted)}
.dots{position:absolute;top:2585px;left:576px;display:flex;gap:10px;align-items:center}
.dot{width:7px;height:7px;border-radius:50%;background:#9a9a9a}
.dot.active{width:11px;height:11px;background:none;border:2px solid var(--ink)}

.footer{position:absolute;left:0;top:2645px;width:1200px;height:59px;display:flex;align-items:center;justify-content:center;font-size:15px;color:var(--muted)}
</style>
</head>
<body>

<header class="hero">
  <div class="hero-coin" role="img" aria-label="Close-up photograph of a gold coin"></div>
  <div class="brand"><span class="brand-mark"></span>Briefhaus Tanner</div>
  <a class="btn" style="left:967px;top:18px" href="#contact">Contact Us</a>
  <h1 class="hero-title">We buy the valuable thing that you sell</h1>
  <p class="hero-text">Do you need help selling an inherited collection? Feel free to <a href="#contact">contact us</a>. We are happy to help. We have been in the stamp and coin trade for nearly 100 years.</p>
  <a class="btn" style="left:83px;top:460px" href="#contact">Contact Us</a>
  <svg class="hero-icon" style="left:258px" viewBox="0 0 24 24" fill="none" stroke="#fff" stroke-width="2"><rect x="2" y="5" width="20" height="14" rx="1"/><path d="M2 6l10 7 10-7"/></svg>
  <svg class="hero-icon" style="left:315px" viewBox="0 0 24 24" fill="none" stroke="#fff" stroke-width="2" stroke-linejoin="round"><path d="M5 3h4l2 5-2.5 1.5a11 11 0 0 0 6 6L16 13l5 2v4a2 2 0 0 1-2 2A17 17 0 0 1 3 5a2 2 0 0 1 2-2z"/></svg>
</header>

<section class="steps">
  <h2 class="section-title">How We Work</h2>
  <div class="step-line"></div>
  <div class="step" style="left:77px">
    <div class="step-icon"><svg width="46" height="34" viewBox="0 0 46 34"><rect width="46" height="34" rx="5" fill="#6b4a2f"/><rect x="6" y="13" width="34" height="8" rx="3" fill="var(--gold)"/></svg></div>
    <div class="step-name">Contact Us</div>
    <p class="step-text">Contact Us via phone<br>or email</p>
  </div>
  <div class="step" style="left:343px">
    <div class="step-icon"><svg width="36" height="46" viewBox="0 0 36 46"><rect width="36" height="46" rx="3" fill="#6b4a2f"/><g stroke="#fff" stroke-width="2.5"><path d="M7 9h22M7 16h22M7 23h22M7 30h22"/></g><rect x="20" y="36" width="11" height="4" rx="2" fill="var(--gold)"/></svg></div>
    <div class="step-name">We Send Form</div>
    <p class="step-text">Fill out your contact and select<br>items you want to sell</p>
  </div>
  <div class="step" style="left:607px">
    <div class="step-icon"><svg width="56" height="56" viewBox="0 0 56 56"><circle cx="28" cy="28" r="24" fill="none" stroke="#c8c8d8" stroke-dasharray="3 3"/><circle cx="40" cy="14" r="12" fill="#6b4a2f"/><circle cx="37" cy="12" r="3" fill="#fff"/><circle cx="43" cy="12" r="3" fill="#fff"/><circle cx="14" cy="42" r="12" fill="#6b4a2f"/><rect x="8" y="37" width="12" height="9" fill="#fff"/><path d="M8 37l6 5 6-5" fill="none" stroke="#6b4a2f" stroke-width="1.5"/></svg></div>
    <div class="step-name">Payment Process</div>
    <p class="step-text">You will receive our purchase form and the mailing label by post so that you can send it</p>
  </div>
  <div class="step" style="left:872px">
    <div class="step-icon"><svg width="34" height="44" viewBox="0 0 34 44"><path d="M11 2h12l-4 8h-4z" fill="#6b4a2f"/><path d="M13 11h8c8 6 13 14 13 21 0 7-6 12-17 12S0 39 0 32c0-7 5-15 13-21z" fill="#6b4a2f"/><text x="17" y="36" text-anchor="middle" font-family="Arial,sans-serif" font-weight="700" font-size="18" fill="#fff">$</text></svg></div>
    <div class="step-name">We Send The Money</div>
    <p class="step-text">We sent the money to you. You can call us or write an e-mail and come to us directly</p>
  </div>
</section>

<section class="buy">
  <div class="deco-ring" style="left:930px;top:-30px;width:560px;height:560px"></div>
  <div class="deco-ring" style="left:-260px;top:60px;width:760px;height:760px;border-width:60px;border-color:rgba(240,240,243,.8)"></div>
  <h2 class="section-title">What We Buy</h2>
  <div class="buy-card" style="left:83px;top:158px;width:504px;height:608px;background:linear-gradient(180deg,#c9a24a 0%,#b08a3a 55%,#6e5424 100%)" role="img" aria-label="Photograph of a pile of gold coins"><span>Gold Stuff</span></div>
  <div class="buy-card" style="left:613px;top:158px;width:504px;height:291px;background:linear-gradient(120deg,#5f7c9a 0%,#7d6a5a 45%,#b45a3a 65%,#2d2d33 100%)" role="img" aria-label="Photograph of assorted postage stamps"><span>Stamps</span></div>
  <div class="buy-card" style="left:613px;top:474px;width:504px;height:292px;background:linear-gradient(150deg,#d6d8dc 0%,#a9acb3 45%,#55585e 100%)" role="img" aria-label="Photograph of a pile of silver coins"><span>Silver Stuff</span></div>
</section>

<section class="cta" id="contact">
  <h2 class="cta-title">Start Sell Your Valuable Thing</h2>
  <a class="btn" style="left:884px;top:83px" href="#contact">Contact Us</a>
</section>

<section class="voices">
  <div class="deco-ring" style="left:1110px;top:50px;width:160px;height:160px;border-width:18px;border-color:rgba(255,255,255,.9)"></div>
  <div class="deco-ring" style="left:-130px;top:300px;width:390px;height:390px;border-width:60px;border-color:rgba(255,255,255,.8)"></div>
  <h2 class="section-title">Our Customers Speak</h2>
  <p class="voices-sub">We have been working with Customers around Swiss</p>
  <div class="quote" style="left:138px"><h3>Efficient Shipping</h3><p>Lorem ipsum dolor sit amet, consectetur adipiscing elit. Auctor neque sed imperdiet nibh lectus feugiat nunc sem.</p></div>
  <div class="quote" style="left:454px"><h3>Easy To Contact</h3><p>Lorem ipsum dolor sit amet, consectetur adipiscing elit. Auctor neque sed imperdiet nibh lectus feugiat nunc sem.</p></div>
  <div class="quote" style="left:771px"><h3>Mindblowing Service</h3><p>Lorem ipsum dolor sit amet, consectetur adipiscing elit. Auctor neque sed imperdiet nibh lectus feugiat nunc sem.</p></div>
  <div class="person" style="left:138px"><div class="avatar" role="img" aria-label="Portrait photo of the customer"></div><b>Lena Hofer</b><small>CEO at Alpen Handel AG</small></div>
  <div class="person" style="left:454px"><div class="avatar" role="img" aria-label="Portrait photo of the customer"></div><b>Mara Keller</b><small>CEO at Alpen Handel AG</small></div>
  <div class="person" style="left:771px"><div class="avatar" role="img" aria-label="Portrait photo of the customer"></div><b>Elin Baumann</b><small>CEO at Alpen Handel AG</small></div>
</section>
<div class="dots"><span class="dot"></span><span class="dot active"></span><span class="dot"></span></div>

<footer class="footer">Copyright © 2020 Briefhaus Tanner</footer>

</body>
</html>
```